Commercial LED Lighting Company need Product Catalog

We need a product catalog for our commercial LED Lighting company. We sell indoor and outdoor lighting fixtures to commercial customers, for commercial purposes. Most of our clients are knowledgeable about our products, and are interested in the technical details of our products.

Our catalog will offer 17 products, with a two page layout for each product. We have a specific vision for the general outline of the product layout. Attached, you will see a competitor's design whose layout we'd like to mimic - the first page for a product will have a large photo up top of a room or space showcasing the product, and the bottom half will be a photo of the product with some general bullet points. The second page will list the various model numbers for the products, along with their technical details. All information needed for the project will be provided, including product photos. We will not include all product photos in our attachment today, as we are limited to how many files we can upload at this time. Also attached is a general outline of the catalog, as well as product details.

Our clients are professionals, and we want to communicate a respect for our clients' know how and industry experience. We also want to maintain our color palate of blue, white and grey. I will also attach our logo to give you a reference.

Sample designs should include a potential cover design, and a two page layout for a single product.

Target Market(s)

LED Lighting Distributors; engineers; professional customers

Industry/Entity Type

Manufacturer

Font styles to use
Sans Serif

Colors
0355a3
cfdeed
85acd3
3276b5
eaf1f7

Requirements
Must have
• All required technical information as outlined in attached documents; all 17 products; the two page layout we have envisioned; our color scheme.

```html
<!DOCTYPE html>
<html lang="en">
<head>
<meta charset="utf-8">
<title>Halvern Commercial — Catalog Cover</title>
<link href="https://fonts.googleapis.com/css2?family=Montserrat:wght@400;600&display=swap" rel="stylesheet">
<style>
  :root {
    --brand-blue: #0355a3;
    --mid-blue: #3276b5;
    --soft-blue: #85acd3;
    --cover-bg: #cfdeed;
    --pale-blue: #eaf1f7;
  }
  html, body {
    margin: 0;
    padding: 0;
    overflow: hidden;
  }
  body {
    width: 848px;
    height: 1200px;
    background: var(--cover-bg);
    font-family: "Montserrat", sans-serif;
  }
  .cover {
    position: relative;
    width: 848px;
    height: 1200px;
    overflow: hidden;
    background: var(--cover-bg);
  }
  .hero-shape {
    position: absolute;
    left: 0;
    top: 0;
    width: 848px;
    height: 1200px;
  }
  .divider {
    position: absolute;
    left: 57px;
    top: 972px;
    width: 345px;
    height: 2px;
    background: var(--mid-blue);
  }
  .brand {
    position: absolute;
    left: 57px;
    top: 1010px;
    width: 600px;
  }
  .brand-name {
    margin: 0;
    font-weight: 600;
    font-size: 46px;
    line-height: 56px;
    color: var(--brand-blue);
    white-space: nowrap;
  }
  .brand-tagline {
    margin: 14px 0 0 0;
    font-weight: 400;
    font-size: 18px;
    line-height: 24px;
    color: var(--mid-blue);
    white-space: nowrap;
  }
</style>
</head>
<body>
  <main class="cover">
    <svg class="hero-shape" viewBox="0 0 595 842" role="img" aria-label="Photograph of a street lamp silhouetted against a glowing orange sunset sky above a city skyline">
      <defs>
        <radialGradient id="sunset-glow" cx="260" cy="330" r="340" gradientUnits="userSpaceOnUse">
          <stop offset="0" stop-color="#fffbe8"/>
          <stop offset="0.16" stop-color="#ffe27a"/>
          <stop offset="0.38" stop-color="#f5a623"/>
          <stop offset="0.68" stop-color="#c96a12"/>
          <stop offset="1" stop-color="#6e3510"/>
        </radialGradient>
      </defs>
      <path d="M330 0 L595 0 L595 290 C560 440 450 555 310 555 C160 555 40 430 40 290 C40 140 160 20 330 0 Z" fill="url(#sunset-glow)"/>
    </svg>

    <div class="divider"></div>

    <div class="brand">
      <p class="brand-name">Halvern Commercial</p>
      <p class="brand-tagline">Precise Light for Working Spaces</p>
    </div>
  </main>
</body>
</html>
```